Health Coach needs a Business Card Design

Need a really modern feminine business card design for a health and lifestyle coach. Needs to use geometric shapes, muted grey/blue/green pastels and black and white - see mood board attached and logo. The client likes black and white, modern, san serif with the use of lines and possibly a shadow leaf as in the mood board. Possibly put the tag line on the back or an icon of the logo. Logo is also attached. An icon of the logo would be great too.

Target Market(s)

Women (some men) aged 30 to 50.

Industry/Entity Type

Business

Contact Information for Business Card

Marla Teveny
e-mail: hello@marlatwell.example
website: marlatwell.example
Phone: +610497258316

The tag line is "A steady path to wellness"

Font styles to use
Sans Serif

Colors
ecf7fb
cfeae6
000000
ffffff
f5f5f5

Requirements
Must have
• Black and white, logo, tag line and details
Nice to have
• Would be nice to incorporate the shadow palm.fern leaves as in the mood board and or geometric lines/shapes - see mood board. Could be either standard rectangle or would be happy with square too.
Should not have
• Flowers or decorations

```html
<!DOCTYPE html>
<html lang="en">
<head>
<meta charset="utf-8">
<title>Marla T — Business Card</title>
<link rel="stylesheet" href="https://fonts.googleapis.com/css2?family=Montserrat:wght@300;400;500&display=swap">
<style>
  :root {
    --page: #ffffff;
    --mint: #cfeae6;
    --ice: #ecf7fb;
    --mist: #f5f5f5;
    --lilac-grey: #e4e2ea;
    --ink: #000000;
    --paper: #ffffff;
    --shadow: rgba(0, 0, 0, 0.45);
  }

  html, body {
    margin: 0;
    padding: 0;
    width: 1200px;
    height: 721px;
    overflow: hidden;
    background: var(--page);
  }

  .card {
    position: relative;
    width: 1200px;
    height: 721px;
    background: var(--page);
  }

  .card__backdrop {
    position: absolute;
    left: 38px;
    top: 38px;
    width: 1122px;
    height: 641px;
    background: linear-gradient(135deg, var(--mint) 0%, var(--ice) 35%, var(--lilac-grey) 65%, var(--mint) 100%);
  }

  .brand-panel {
    position: absolute;
    left: 224px;
    top: 254px;
    width: 748px;
    height: 201px;
    box-sizing: border-box;
    background: var(--paper);
    border: 2px solid var(--ink);
    box-shadow: 10px 12px 14px var(--shadow);
  }

  .brand-panel__name {
    position: absolute;
    left: 0;
    right: 0;
    top: 62px;
    margin: 0;
    text-align: center;
    font-family: "Montserrat", sans-serif;
    font-weight: 300;
    font-size: 52px;
    letter-spacing: 5px;
    line-height: 1;
    color: var(--ink);
  }

  .brand-panel__tagline {
    position: absolute;
    left: 0;
    right: 0;
    top: 160px;
    margin: 0;
    text-align: center;
    font-family: "Montserrat", sans-serif;
    font-weight: 500;
    font-size: 13px;
    line-height: 1;
    letter-spacing: 3.4px;
    text-transform: uppercase;
    color: var(--ink);
  }
</style>
</head>
<body>
  <main class="card">
    <div class="card__backdrop" role="img" aria-label="Diagonal pastel stripe pattern in mint, grey and lilac"></div>
    <section class="brand-panel">
      <h1 class="brand-panel__name">Marla T</h1>
      <p class="brand-panel__tagline">A steady path to wellness</p>
    </section>
  </main>
</body>
</html>
```